The Farrowdale Penick Firm

We are a real estate and business acquisition services company that provides consulting services to large companies and individuals. The company provided nationwide services to companies looking to expand through opening new locations or buying other companies in their field. We work very close with attorneys, accountants, banks/financial institutions and high level executives and business owners.

Target Market(s)

CEO, VP, business owners and bankers.

Industry/Entity Type

Real Estate

Requirements
Must have
• I am looking for a design that looks very professional and has a classic, trustworthy, professional feeling. I want the letterhead and return address to look formal and official so this it is not tossed out as junk mail. FP or FPF can be used in a logo style part but that is not required. Our tag line is "Real Estate and Business Acquisition Services". This should be on the letter head but not on the return address. It does not need a lot of color but I will leave that to your tasteful choice. It should be rich and formal looking.
Should not have
• I do not want anything that looks like a cartoon drawing or figure. Use font that gives a strong trustworthy look. We are not a law firm so no scales or gavels. A law firm sort of look or feel is OK.

```html
<!DOCTYPE html>
<html lang="en">
<head>
<meta charset="utf-8">
<title>The Farrowdale Penick Firm — Stationery</title>
<link rel="stylesheet" href="https://fonts.googleapis.com/css2?family=Cinzel:wght@400;600&family=Montserrat:wght@300;400&display=swap">
<style>
  :root {
    --stage: #e6e3de;
    --paper: #ffffff;
    --firm-blue: #2f4a9a;
    --card-blue: #1f3f9e;
    --accent-green: #8ccf5a;
    --band-grey: #bcbcbc;
    --card-grey: #b9b9b9;
    --ink-grey: #8a8a8a;
    --line: #9a9a9a;
    --shadow: 0 4px 14px rgba(0,0,0,.22);
  }
  * { box-sizing: border-box; margin: 0; padding: 0; }
  html, body { width: 1200px; height: 900px; overflow: hidden; }
  body { background: var(--stage); font-family: "Montserrat", sans-serif; }
  .stationery { position: relative; width: 1200px; height: 900px; }

  .firm-name { font-family: "Cinzel", serif; color: var(--firm-blue); letter-spacing: .04em; font-weight: 600; }
  .brand-square { display: block; background: var(--accent-green); margin: 0 auto; }
  .tagline { font-weight: 300; text-transform: uppercase; letter-spacing: .14em; color: var(--ink-grey); }

  /* Letterhead */
  .letterhead { position: absolute; left: 50px; top: 80px; width: 500px; height: 660px;
    background: var(--paper); box-shadow: var(--shadow); }
  .letterhead__brand { text-align: center; padding-top: 30px; }
  .letterhead__brand .brand-square { width: 30px; height: 30px; margin-bottom: 10px; }
  .letterhead__brand .firm-name { font-size: 20px; }
  .letterhead__brand .tagline { font-size: 7.5px; margin-top: 4px; }
  .letterhead__footer { position: absolute; left: 0; right: 0; bottom: 0; height: 38px;
    background: var(--band-grey); color: #fff; display: flex; align-items: center;
    justify-content: space-between; padding: 0 28px; font-size: 8px; letter-spacing: .12em; text-transform: uppercase; }

  /* Envelope */
  .envelope { position: absolute; left: 600px; top: 80px; width: 560px; height: 230px;
    background: var(--paper); box-shadow: var(--shadow); }
  .envelope__return { position: absolute; left: 16px; top: 14px; display: flex; gap: 10px; align-items: flex-start; }
  .envelope__return .brand-square { width: 26px; height: 26px; margin: 2px 0 0; }
  .envelope__return .firm-name { font-size: 11px; line-height: 1.35; }
  .envelope__stamp { position: absolute; right: 14px; top: 14px; width: 40px; height: 40px; border: 1px solid var(--line); }
  .envelope__window { position: absolute; left: 58px; top: 140px; width: 260px; height: 60px; border: 1px solid var(--line); }

  /* Business cards */
  .card { position: absolute; width: 210px; height: 120px; border-radius: 8px; box-shadow: var(--shadow); }
  .card--front { left: 620px; top: 390px; background: var(--paper); text-align: center; padding-top: 22px; }
  .card--front .brand-square { width: 24px; height: 24px; margin-bottom: 10px; }
  .card--front .firm-name { font-size: 12px; }
  .card--front .tagline { font-size: 5px; margin-top: 3px; }
  .card--back { padding: 20px 14px 10px; color: #fff; text-align: center; font-size: 7px; line-height: 1.6; }
  .card--grey { left: 870px; top: 390px; background: var(--card-grey); }
  .card--blue { left: 620px; top: 540px; background: var(--card-blue); }
  .card__person { font-family: "Cinzel", serif; font-size: 11px; letter-spacing: .06em; }
  .card--grey .card__person { color: var(--firm-blue); }
  .card__email { color: var(--accent-green); }
  .card--grey .card__email { color: #fff; }
  .card__firm { position: absolute; right: 14px; bottom: 10px; text-align: right; text-transform: uppercase;
    letter-spacing: .08em; font-size: 5.5px; line-height: 1.6; }
  .card--grey .card__firm { color: var(--firm-blue); }
</style>
</head>
<body>
<main class="stationery">

  <section class="letterhead" aria-label="Letterhead">
    <header class="letterhead__brand">
      <span class="brand-square"></span>
      <h1 class="firm-name">The Farrowdale Penick Firm</h1>
      <p class="tagline">Real Estate and Business Acquisition Services</p>
    </header>
    <footer class="letterhead__footer">
      <span>200-4410 Harbin Ridge Road Brentwood, TN 37027</span>
      <span>615.555.0142</span>
      <span>www.farrowdalepenick.com</span>
    </footer>
  </section>

  <section class="envelope" aria-label="Envelope">
    <div class="envelope__return">
      <span class="brand-square"></span>
      <address class="firm-name" style="font-style:normal">
        The Farrowdale Penick Firm<br>
        200-4410 Harbin Ridge Road<br>
        Brentwood, TN 37027
      </address>
    </div>
    <div class="envelope__stamp"></div>
    <div class="envelope__window"></div>
  </section>

  <section class="card card--front" aria-label="Business card front">
    <span class="brand-square"></span>
    <h2 class="firm-name">The Farrowdale Penick Firm</h2>
    <p class="tagline">Real Estate and Business Acquisition Services</p>
  </section>

  <section class="card card--back card--grey" aria-label="Business card back">
    <p class="card__person">Daniel Hargrove</p>
    <p>Managing Partner</p>
    <p class="card__email">dhargrove@farrowdalepenick.com</p>
    <p>615.555.0142 &nbsp; 615.555.0143</p>
    <p class="card__firm">The Farrowdale Penick Firm<br>200-4410 Harbin Ridge Road Brentwood, TN 37027</p>
  </section>

  <section class="card card--back card--blue" aria-label="Business card back">
    <p class="card__person">Martin Ellery</p>
    <p>Senior Consultant</p>
    <p class="card__email">mellery@farrowdalepenick.com</p>
    <p>615.555.0142 &nbsp; 615.555.0144</p>
    <p class="card__firm">The Farrowdale Penick Firm<br>200-4410 Harbin Ridge Road Brentwood, TN 37027</p>
  </section>

</main>
</body>
</html>
```